Design some Business Cards for Kelvo Systems

I need a design for business cards. I have an existing logo.

I am a sole trader (work for myself) and I provide computer and IT technology support services to small businesses in Australia. I advise business owners on how to best use and manage their IT systems and computers and I provide onsite computer troubleshooting services.
The style should reflect the professional nature of my work.
I would likely favour a simpler and clean design.

The artwork needs to be:
Single sided (just the front of the card)
89mm x 54mm in size.
Full colour.
To be printed on white stock (paper)

Details that need to be included on the business cards are:
Logo
Name Miles BBBBBBBB
Email address miles@kelvosys.example
Phone number 2222 222 222

The exact details will be supplied at the end of the contest for the final artwork.
Final artwork would need to be print ready – I can provide examples of what they need to look like.

```html
<!DOCTYPE html>
<html lang="en">
<head>
<meta charset="utf-8">
<title>Kelvo Systems – Business Card</title>
<link rel="stylesheet" href="https://fonts.googleapis.com/css2?family=Dosis:wght@500&family=Lato:wght@400;700&display=swap">
<style>
  :root {
    --backdrop: #2b2d30;
    --card-white: #f4f5f6;
    --brand-grey: #4a4c50;
    --tagline: #5d6066;
    --tagline-soft: #9a9da3;
    --band-top: #2a7cc4;
    --band-bottom: #1b5f9f;
    --strip: #2f87cf;
    --band-edge: #14508a;
    --mark: #2f6db0;
    --ink-light: #ffffff;
    --ink-muted: #dbe9f6;
  }
  html, body {
    margin: 0;
    padding: 0;
    width: 1200px;
    height: 675px;
    overflow: hidden;
    background: var(--backdrop);
  }
  .card {
    position: absolute;
    left: 150px;
    top: 64px;
    width: 900px;
    height: 546px;
    background: var(--card-white);
    overflow: hidden;
    box-shadow: 0 10px 30px rgba(0,0,0,0.45);
  }
  .card__band {
    position: absolute;
    left: 0;
    top: 0;
    width: 900px;
    height: 546px;
  }
  .brand {
    position: absolute;
    left: 60px;
    top: 92px;
    display: flex;
    align-items: center;
  }
  .brand__mark {
    width: 120px;
    height: 120px;
    border-radius: 50%;
    background: var(--mark);
    flex: none;
  }
  .brand__text {
    margin-left: 36px;
  }
  .brand__name {
    font-family: "Dosis", sans-serif;
    font-weight: 500;
    font-size: 80px;
    line-height: 0.9;
    color: var(--brand-grey);
    letter-spacing: -1px;
    margin: 0;
  }
  .brand__tagline {
    font-family: "Lato", sans-serif;
    font-size: 24px;
    line-height: 1.1;
    color: var(--tagline);
    margin: 6px 0 0 4px;
    letter-spacing: 0.5px;
  }
  .brand__tagline--soft {
    color: var(--tagline-soft);
    font-size: 21px;
    margin-top: 2px;
  }
  .holder {
    position: absolute;
    left: 60px;
    top: 398px;
    font-family: "Lato", sans-serif;
    font-weight: 700;
    font-size: 30px;
    letter-spacing: 1px;
    color: var(--ink-light);
    margin: 0;
  }
  .contacts {
    position: absolute;
    left: 60px;
    top: 492px;
    font-family: "Lato", sans-serif;
    font-size: 21px;
    color: var(--ink-muted);
    display: flex;
    gap: 14px;
    margin: 0;
  }
  .contacts__sep {
    opacity: 0.6;
  }
</style>
</head>
<body>
  <div class="card">
    <svg class="card__band" viewBox="0 0 900 546" aria-hidden="true">
      <defs>
        <linearGradient id="bandFill" x1="0" y1="0" x2="0" y2="1">
          <stop offset="0" stop-color="var(--band-top)"/>
          <stop offset="1" stop-color="var(--band-bottom)"/>
        </linearGradient>
      </defs>
      <path d="M0 330 H520 L545 312 L570 330 H900 V546 H0 Z" fill="var(--band-edge)"/>
      <path d="M0 336 H520 L545 318 L570 336 H900 V546 H0 Z" fill="url(#bandFill)"/>
      <rect x="0" y="470" width="900" height="76" fill="var(--strip)"/>
    </svg>

    <div class="brand">
      <div class="brand__mark"></div>
      <div class="brand__text">
        <p class="brand__name">Kelvo Systems</p>
        <p class="brand__tagline">Computer and IT Problems Solved</p>
        <p class="brand__tagline brand__tagline--soft">Computer and IT Problems Solved</p>
      </div>
    </div>

    <p class="holder">FIRSTNAME SURNAME</p>

    <p class="contacts">
      <span class="contacts__item">miles@kelvosys.example</span>
      <span class="contacts__sep">|</span>
      <span class="contacts__item">2222 222 222</span>
      <span class="contacts__sep">|</span>
      <span class="contacts__item">www.kelvosys.example</span>
    </p>
  </div>
</body>
</html>
```